Corvale Spine & Joint Business Card

Need a business card using the logo provided. I want brand side of the card to be grey with the logo in the center of the card in white.

On the other side I leave to the designers

Target Market(s)

Personal Injury Attorneys

Industry/Entity Type

Medical

Contact Information for Business Card

Name, CEO. Cell Phone, (Brookhaven, Address, Phone) (Linwood, Address, Phone) (Ashford Falls, Address, Phone)

Colors

Designer to choose only greyscale colors for use in the design.

Requirements
Must have
• Logo by itself on one side

```html
<!DOCTYPE html>
<html lang="en">
<head>
<meta charset="utf-8">
<title>Corvale Spine &amp; Joint Business Card</title>
<link href="https://fonts.googleapis.com/css2?family=Work+Sans:wght@400;500;600&display=swap" rel="stylesheet">
<style>
  :root {
    --backdrop: #cfcfcf;
    --card: #93b0b8;
    --ink-white: #ffffff;
    --ink-blue: #2f6db3;
    --card-shadow: rgba(40, 50, 55, 0.28);
  }
  * { margin: 0; padding: 0; box-sizing: border-box; }
  html, body { width: 1200px; height: 800px; overflow: hidden; }
  body {
    background: var(--backdrop);
    font-family: "Work Sans", Arial, sans-serif;
    position: relative;
  }
  .card {
    position: absolute;
    width: 560px;
    height: 320px;
    background: var(--card);
    border-radius: 24px;
    box-shadow: 0 10px 28px var(--card-shadow);
  }
  .card--info { left: 90px; top: 80px; }
  .card--brand { left: 550px; top: 400px; }

  .contact {
    position: absolute;
    left: 40px;
    top: 32px;
    color: var(--ink-white);
    font-size: 12.5px;
    line-height: 15px;
  }
  .contact__name {
    color: var(--ink-blue);
    font-weight: 600;
    font-size: 17px;
    letter-spacing: 0.5px;
    text-transform: uppercase;
    line-height: 20px;
  }
  .contact__phone { display: flex; align-items: center; gap: 5px; }
  .contact__phone svg { width: 10px; height: 11px; fill: var(--ink-blue); flex: none; }
  .office { margin-top: 9px; }
  .office__city { color: var(--ink-blue); font-weight: 600; font-size: 13px; }

  .brand-name {
    position: absolute;
    inset: 0;
    display: flex;
    flex-direction: column;
    align-items: center;
    justify-content: center;
    color: var(--ink-white);
    font-weight: 500;
    text-transform: uppercase;
    text-align: center;
  }
  .brand-name__main { font-size: 54px; letter-spacing: 8px; line-height: 60px; }
  .brand-name__sub { font-size: 22px; letter-spacing: 7px; line-height: 30px; }
</style>
</head>
<body>

<section class="card card--info" aria-label="Contact side">
  <div class="contact">
    <p class="contact__name">Daniel Reyes</p>
    <p class="contact__title">President</p>
    <p class="contact__phone">
      <svg viewBox="0 0 10 14" aria-hidden="true"><path d="M2 0h6a2 2 0 0 1 2 2v10a2 2 0 0 1-2 2H2a2 2 0 0 1-2-2V2a2 2 0 0 1 2-2zm0 2v9h6V2z"/></svg>
      555-014-2273
    </p>

    <div class="office">
      <p class="office__city">Brookhaven</p>
      <p>2140 Harbor View Road</p>
      <p>Fairmont, Ohio 44120</p>
      <p class="contact__phone">
        <svg viewBox="0 0 12 12" aria-hidden="true"><path d="M2.5 0.5l2 2.5-1.2 1.3c.7 1.6 1.8 2.7 3.4 3.4L8 6.5l2.5 2-1.3 2.5C4.5 10.8 1.2 7.5 0.5 1.8z"/></svg>
        555-014-2273
      </p>
    </div>

    <div class="office">
      <p class="office__city">Linwood</p>
      <p>2140 Harbor View Road</p>
      <p>Fairmont, Ohio 44120</p>
      <p class="contact__phone">
        <svg viewBox="0 0 12 12" aria-hidden="true"><path d="M2.5 0.5l2 2.5-1.2 1.3c.7 1.6 1.8 2.7 3.4 3.4L8 6.5l2.5 2-1.3 2.5C4.5 10.8 1.2 7.5 0.5 1.8z"/></svg>
        555-014-2273
      </p>
    </div>

    <div class="office">
      <p class="office__city">Ashford Falls</p>
      <p>2140 Harbor View Road</p>
      <p>Fairmont, Ohio 44120</p>
      <p class="contact__phone">
        <svg viewBox="0 0 12 12" aria-hidden="true"><path d="M2.5 0.5l2 2.5-1.2 1.3c.7 1.6 1.8 2.7 3.4 3.4L8 6.5l2.5 2-1.3 2.5C4.5 10.8 1.2 7.5 0.5 1.8z"/></svg>
        555-014-2273
      </p>
    </div>
  </div>
</section>

<section class="card card--brand" aria-label="Brand side">
  <h1 class="brand-name">
    <span class="brand-name__main">Corvale</span>
    <span class="brand-name__sub">Spine &amp; Joint</span>
  </h1>
</section>

</body>
</html>
```